Mobile Spray tanner needs a Mobile Spray tanning business card design

I need a simple but eye-catching business card design. I would like the business card to be in two colours only (Hot pink background with black Silhouette & black writing). I would like the white behind the silhouette removed and the other bits on the silhouette removed (to be just a black silhouette with a hot pink bikini on). I would like the black writing to be aesthetically pleasing and quite artistic, but easy to read). Thank you very much

```html
<!DOCTYPE html>
<html lang="en">
<head>
<meta charset="utf-8">
<title>Sunkissed Shapes Mobile Spray Tanning – Business Card</title>
<link rel="stylesheet" href="https://fonts.googleapis.com/css2?family=Libre+Baskerville&display=swap">
<style>
  :root {
    --backdrop: #e9e6e3;
    --card: #fbfbfb;
    --hot-pink: #e95cb4;
    --ink: #1a1a1a;
    --silhouette: #0b0b0b;
  }
  html, body {
    margin: 0;
    padding: 0;
    width: 1200px;
    height: 960px;
    overflow: hidden;
    background: var(--backdrop);
  }
  .stage {
    width: 1200px;
    height: 960px;
    display: flex;
    align-items: center;
    justify-content: center;
  }
  .business-card {
    position: relative;
    width: 500px;
    height: 860px;
    background: var(--card);
    box-shadow: 0 10px 30px rgba(0,0,0,0.18);
    font-family: "Libre Baskerville", "Palatino Linotype", serif;
    color: var(--ink);
    overflow: hidden;
  }
  .accent-top {
    position: absolute;
    top: 0; left: 0; right: 0;
    height: 8px;
    background: var(--hot-pink);
  }
  .accent-bottom {
    position: absolute;
    bottom: 0; left: 0; right: 0;
    height: 8px;
    background: var(--silhouette);
  }
  .business-name {
    position: absolute;
    top: 62px;
    left: 62px;
    margin: 0;
    font-weight: 400;
    font-size: 34px;
    line-height: 1.08;
    letter-spacing: 0.02em;
    text-transform: uppercase;
  }
  .business-name span { display: block; }
  .business-name .line-wide { font-size: 38px; }
  .figure-art {
    position: absolute;
    top: 270px;
    left: 120px;
    width: 280px;
    height: 470px;
  }
  .phone {
    position: absolute;
    bottom: 54px;
    left: 62px;
    margin: 0;
    font-size: 30px;
    letter-spacing: 0.01em;
  }
</style>
</head>
<body>
  <main class="stage">
    <article class="business-card">
      <div class="accent-top"></div>
      <h1 class="business-name">
        <span>Sunkissed Shapes</span>
        <span>Mobile</span>
        <span class="line-wide">Spray Tanning</span>
      </h1>
      <svg class="figure-art" viewBox="0 0 280 470" role="img" aria-label="Black silhouette of a kneeling woman wearing a hot pink bikini">
        <defs>
          <linearGradient id="figureTone" x1="0" y1="0" x2="0" y2="1">
            <stop offset="0" stop-color="#111111"/>
            <stop offset="0.45" stop-color="#3a1a2e"/>
            <stop offset="0.6" stop-color="#111111"/>
            <stop offset="1" stop-color="#0b0b0b"/>
          </linearGradient>
        </defs>
        <rect x="0" y="0" width="280" height="470" rx="6" fill="url(#figureTone)"/>
      </svg>
      <p class="phone">M. 0400 126 958</p>
      <div class="accent-bottom"></div>
    </article>
  </main>
</body>
</html>
```